"Dario Quillon" Business Card

Friends

My name is "Dario Quillon" and I need your help! I need a new business card for my personal use.

As background, "Dario Quillon" is actually an alias that I use when I meet women. Please use your creative skills to create an amazing business card for me to use!

In addition to including my name and contact details (see the "Must Have" section), you may wish to add a catchphrase or a title if you think it would help me :)

For background, please see:

http://www.dailybrightwire.com/2013/07/23/morton-feld-dario-quillon_n_5129847.html

Looking forward to seeing what you can do for me.

Hugs and kisses,

Dario Quillon [courtesy of PixelHarbor]

Target Market(s)

Adult women in New York City...or anywhere really.

Industry/Entity Type

Business

Requirements
Must have
• Please include the following details:

Dario Quillon
P: +1-555-3QUILLN
E: secrets@darioquillon-mail.com
Nice to have
• You might include a catchphrase, like "Quillon is my surname But you can call me Mr Smoothstep".

Or perhaps a title, like "Dario Quillon, Head of Sexy Times".

You're creative...I will leave the details to you my friends.
Should not have
• Any references to my actual name...because then, what's the point in using an alias?

```html
<!DOCTYPE html>
<html lang="en">
<head>
<meta charset="utf-8">
<title>Dario Quillon — Business Card</title>
<link rel="stylesheet" href="https://fonts.googleapis.com/css2?family=Arimo:wght@400;700&display=swap">
<style>
  :root {
    --page-bg: #e9e6e3;
    --card-black: #050505;
    --card-charcoal: #1a1a1a;
    --suit-dark: #232323;
    --suit-mid: #3a3a3a;
    --shirt-white: #e8e8e8;
    --tie-red: #a3141d;
    --accent-pink: #cf1a6c;
    --name-white: #ffffff;
    --band-red-dark: #5e0404;
    --band-red: #b30d0d;
    --silhouette: #1c0000;
  }
  * { box-sizing: border-box; margin: 0; padding: 0; }
  html, body {
    width: 1200px;
    height: 867px;
    overflow: hidden;
    background: var(--page-bg);
    font-family: "Arimo", Arial, sans-serif;
  }
  .canvas { position: relative; width: 1200px; height: 867px; }

  .card {
    position: absolute;
    width: 620px;
    height: 354px;
    border-radius: 14px;
    background: var(--card-black);
    overflow: hidden;
    box-shadow: 0 10px 28px rgba(0,0,0,0.28);
  }

  /* Front */
  .card-front { left: 60px; top: 70px; }
  .suit-photo {
    position: absolute;
    top: 0; right: 0;
    width: 72%;
    height: 100%;
    background:
      linear-gradient(90deg, transparent 0%, transparent 47%, var(--tie-red) 50%, var(--tie-red) 56%, transparent 59%),
      linear-gradient(90deg, var(--card-black) 0%, var(--suit-dark) 18%, var(--suit-mid) 34%, var(--shirt-white) 42%, var(--shirt-white) 64%, var(--suit-mid) 72%, var(--suit-dark) 88%, var(--card-charcoal) 100%);
    -webkit-mask-image: linear-gradient(90deg, transparent 0%, #000 22%);
            mask-image: linear-gradient(90deg, transparent 0%, #000 22%);
  }
  .front-details {
    position: absolute;
    left: 62px;
    top: 196px;
  }
  .holder-name {
    color: var(--name-white);
    font-weight: 700;
    font-size: 17px;
    font-style: italic;
    margin-bottom: 20px;
  }
  .contact-line {
    color: var(--accent-pink);
    font-size: 16px;
    line-height: 19px;
    font-style: italic;
  }

  /* Back */
  .card-back { left: 520px; top: 460px; }
  .catchphrase {
    position: absolute;
    left: 72px;
    top: 140px;
    color: var(--accent-pink);
    font-size: 19px;
    line-height: 22px;
    font-style: italic;
  }
  .red-band {
    position: absolute;
    top: 0; right: 0;
    width: 112px;
    height: 100%;
    background: linear-gradient(90deg, var(--band-red-dark), var(--band-red));
  }
  .figure-silhouette {
    position: absolute;
    left: 10px;
    top: 60px;
    width: 70px;
    height: 264px;
    border-radius: 30px 30px 6px 6px;
    background: linear-gradient(180deg, var(--silhouette), rgba(28,0,0,0.75));
  }
</style>
</head>
<body>
  <main class="canvas">
    <section class="card card-front" aria-label="Card front">
      <div class="suit-photo" role="img" aria-label="Photo of a man's chest in a dark suit, white shirt and red tie"></div>
      <div class="front-details">
        <p class="holder-name">Dario Quillon</p>
        <p class="contact-line">+1-555-3QUILLN</p>
        <p class="contact-line">secrets@darioquillon-mail.com</p>
      </div>
    </section>

    <section class="card card-back" aria-label="Card back">
      <p class="catchphrase">“Quillon is my surname,<br>But you can call me Mr Smoothstep”</p>
      <div class="red-band">
        <div class="figure-silhouette" role="img" aria-label="Silhouette illustration of a man in a suit standing with hands in pockets"></div>
      </div>
    </section>
  </main>
</body>
</html>
```